Design a Professional Business Card for Vello Marra

Design a business card for Vello Marra, we are a National Sport Court Company.

West Region Address: 4172 Glen Harrow Ct, Suite #210 Englewood, Colorado 80112
East Region Address: 7316 38th Ave W, Bradenton, Florida 34210

Target Market(s)

High End Residential & Institutional Clients

Industry/Entity Type

Design & Construction

Contact Information for Business Card

Logo/Brand/Colors/ name, number (provided in comments)

Requirements
Must have
• Colors only provided in logo
Should not have
• Any other colors not in existing logo (attached)

```html
<!DOCTYPE html>
<html lang="en">
<head>
<meta charset="utf-8">
<title>Vello Marra Business Card</title>
<link href="https://fonts.googleapis.com/css2?family=Montserrat:wght@400;500;700&display=swap" rel="stylesheet">
<style>
  :root {
    --navy: #1b2f5e;
    --green: #17703a;
    --white: #ffffff;
    --ink: #2b2b2b;
    --backdrop: #3b3b3d;
  }
  * { margin: 0; padding: 0; box-sizing: border-box; }
  html, body {
    width: 1200px; height: 1200px; overflow: hidden;
    background: var(--backdrop);
    font-family: "Montserrat", sans-serif;
  }
  .card {
    position: absolute; left: 120px;
    width: 960px; height: 549px;
    border-radius: 40px; overflow: hidden;
  }
  .card-front { top: 40px; background: var(--white); }
  .card-back { top: 611px; background: var(--navy); }

  .front-wave { position: absolute; inset: 0; width: 960px; height: 549px; }

  .contact-block { position: absolute; left: 70px; top: 175px; }
  .person-name {
    color: var(--navy); font-weight: 700; font-size: 32px;
    letter-spacing: 0.5px; text-transform: uppercase;
  }
  .person-title { color: var(--ink); font-size: 28px; font-weight: 500; margin-top: 2px; }
  .contact-list { list-style: none; margin-top: 26px; }
  .contact-list li {
    display: flex; align-items: center; gap: 16px;
    color: var(--ink); font-size: 26px; font-weight: 500; line-height: 46px;
  }
  .contact-list svg { width: 28px; height: 28px; flex: none; }

  .brand { position: absolute; display: flex; align-items: center; }
  .brand-front { left: 560px; top: 120px; gap: 26px; }
  .brand-dot { border-radius: 50%; flex: none; }
  .brand-front .brand-dot { width: 110px; height: 110px; background: var(--navy); }
  .brand-name { font-weight: 700; text-transform: uppercase; line-height: 0.95; }
  .brand-front .brand-name { color: var(--navy); font-size: 62px; letter-spacing: 3px; }

  .website {
    position: absolute; right: 60px; bottom: 50px;
    color: var(--white); font-size: 26px; font-weight: 500; letter-spacing: 0.5px;
  }

  .brand-back { left: 50%; top: 50%; transform: translate(-50%, -50%); gap: 40px; }
  .brand-back .brand-dot { width: 170px; height: 170px; background: var(--green); }
  .brand-back .brand-name { color: var(--white); font-size: 96px; letter-spacing: 5px; }
</style>
</head>
<body>
  <section class="card card-front">
    <svg class="front-wave" viewBox="0 0 960 549" aria-hidden="true">
      <path d="M0 503 L540 503 C610 503 630 405 705 405 L960 405" fill="none" stroke="var(--green)" stroke-width="8"/>
      <path d="M0 515 L545 515 C615 515 635 417 710 417 L960 417 L960 549 L0 549 Z" fill="var(--navy)"/>
    </svg>

    <div class="brand brand-front">
      <span class="brand-dot"></span>
      <span class="brand-name">Vello<br>Marra</span>
    </div>

    <div class="contact-block">
      <p class="person-name">Dorian L. Reeve, MLA</p>
      <p class="person-title">CEO &amp; Founder</p>
      <ul class="contact-list">
        <li>
          <svg viewBox="0 0 24 24" aria-hidden="true"><rect x="6" y="2" width="12" height="20" rx="2" fill="none" stroke="var(--navy)" stroke-width="2"/><circle cx="12" cy="18" r="1.2" fill="var(--navy)"/></svg>
          (303) 555-0147
        </li>
        <li>
          <svg viewBox="0 0 24 24" aria-hidden="true"><path d="M6.6 10.8a15 15 0 0 0 6.6 6.6l2.2-2.2a1 1 0 0 1 1-.25 11.4 11.4 0 0 0 3.6.57 1 1 0 0 1 1 1V20a1 1 0 0 1-1 1A17 17 0 0 1 3 4a1 1 0 0 1 1-1h3.5a1 1 0 0 1 1 1c0 1.25.2 2.45.57 3.57a1 1 0 0 1-.25 1z" fill="var(--navy)"/></svg>
          1-800-555-0192
        </li>
        <li>
          <svg viewBox="0 0 24 24" aria-hidden="true"><rect x="2" y="5" width="20" height="14" fill="var(--navy)"/><path d="M2 5 L12 13 L22 5 M2 19 L9 11 M22 19 L15 11" fill="none" stroke="var(--white)" stroke-width="1.5"/></svg>
          dorian@vellomarraco.com
        </li>
      </ul>
    </div>

    <p class="website">www.vellomarra.com</p>
  </section>

  <section class="card card-back">
    <div class="brand brand-back">
      <span class="brand-dot"></span>
      <span class="brand-name">Vello<br>Marra</span>
    </div>
  </section>
</body>
</html>
```